Tech business card design

We need an amazing business card design for our new business 'Brakka' a marketing tech startup based in Sydney, Australia. We provide an online marketplace for businesses to search and buy advertising media, connect with service providers and learn more about marketing. We wish to communicate 'cool tech', reliability and professionalism and design based around our logo.

Target Market(s)

Business Owners

Contact Information for Business Card

Name
Position
Email Address
Website
Phone Number

Font styles to use
Other font styles liked:
• Avenir & Avenir Next

Colors

Designer to choose colors to be used in the design.

```html
<!DOCTYPE html>
<html lang="en">
<head>
<meta charset="UTF-8">
<title>Brakka Business Card</title>
<link href="https://fonts.googleapis.com/css2?family=Nunito+Sans:wght@400;800;900&display=swap" rel="stylesheet">
<style>
  :root {
    --navy: #14134a;
    --navy-soft: #1c1b5a;
    --white: #ffffff;
    --ink: #1a1a2e;
    --backdrop: #d9dadd;
  }
  * { margin: 0; padding: 0; box-sizing: border-box; }
  html, body {
    width: 1200px; height: 800px; overflow: hidden;
    background: var(--backdrop);
    font-family: "Nunito Sans", Arial, sans-serif;
  }
  .stage {
    width: 1200px; height: 800px;
    display: flex; align-items: center; justify-content: center; gap: 40px;
  }
  .card {
    width: 540px; height: 310px; position: relative; overflow: hidden;
    box-shadow: 0 6px 18px rgba(0,0,0,0.18);
  }
  /* Back side */
  .card-back { background: var(--navy); }
  .card-back .pattern {
    position: absolute; inset: 0;
    background: radial-gradient(ellipse at center, var(--navy-soft) 0%, var(--navy) 75%);
  }
  .card-back .wordmark {
    position: absolute; left: 50%; top: 50%; transform: translate(-50%, -50%);
    color: var(--white); font-weight: 900; font-size: 44px; letter-spacing: -1px;
  }
  /* Front side */
  .card-front { background: var(--white); }
  .card-front .band {
    position: absolute; left: 0; top: 22px; width: 100%; height: 118px;
    background: var(--navy);
    display: flex; align-items: center; justify-content: center;
  }
  .card-front .wordmark {
    color: var(--white); font-weight: 900; font-size: 92px; letter-spacing: -3px; line-height: 1;
  }
  .details {
    position: absolute; left: 40px; right: 30px; top: 180px;
    display: flex; align-items: center; color: var(--ink);
  }
  .identity { text-align: right; padding-right: 20px; border-right: 1.5px solid var(--ink); }
  .identity .name { font-weight: 800; font-size: 20px; line-height: 1.1; }
  .identity .position { font-size: 18px; line-height: 1.2; }
  .contacts { list-style: none; padding-left: 20px; font-size: 18px; line-height: 1.4; }
  .contacts li { display: flex; align-items: center; gap: 10px; }
  .contacts svg { width: 15px; height: 15px; flex: none; }
</style>
</head>
<body>
<main class="stage">
  <section class="card card-back">
    <div class="pattern" role="img" aria-label="Faint repeating wordmark pattern on navy"></div>
    <div class="wordmark">Brakka</div>
  </section>

  <section class="card card-front">
    <div class="band"><span class="wordmark">Brakka</span></div>
    <div class="details">
      <div class="identity">
        <div class="name">Your Name</div>
        <div class="position">Your Position</div>
      </div>
      <ul class="contacts">
        <li>
          <svg viewBox="0 0 16 16" aria-hidden="true"><path d="M3 1l3 3-1.5 2a9 9 0 0 0 5.5 5.5L12 10l3 3-2 2C7 15 1 9 1 3z" fill="var(--ink)"/></svg>
          123 456 78
        </li>
        <li>
          <svg viewBox="0 0 16 16" aria-hidden="true"><rect x="1" y="3" width="14" height="10" fill="var(--ink)"/><path d="M1 3l7 6 7-6" stroke="var(--white)" stroke-width="1.3" fill="none"/></svg>
          name@yourmail.com
        </li>
        <li>
          <svg viewBox="0 0 16 16" aria-hidden="true"><circle cx="8" cy="8" r="7" fill="var(--ink)"/><path d="M1 8h14M8 1c-3 4-3 10 0 14M8 1c3 4 3 10 0 14" stroke="var(--white)" stroke-width="1" fill="none"/></svg>
          www.yoursite.com
        </li>
      </ul>
    </div>
  </section>
</main>
</body>
</html>
```